Corvalla Sponsored Content Images

Image spec: 1.91:1 ratio (1200x627px)We require 6x variations of this image: See the excel attached for the copy.Each image should contain the ZEMBO logo, 2 headshots if posible, a designed background and a CTA button + the copy.Please make sure that all of the copy is clear and big enough to read so it can be read on mobile devices.

Target Market(s)

This is for Corvalla ads to Executives of mid-market companies

Font styles to use
Sans Serif

Colors

Designer to choose colors to be used in the design.

```html
<!DOCTYPE html>
<html lang="en">
<head>
<meta charset="utf-8">
<title>ZEMBO Webinar Sponsored Content Set</title>
<link href="https://fonts.googleapis.com/css2?family=Source+Sans+3:ital,wght@0,300;0,400;0,700;1,300;1,400&display=swap" rel="stylesheet">
<style>
  :root {
    --board: #b6b4b6;
    --navy: #0b2452;
    --navy-mid: #123a78;
    --ink-black: #121214;
    --indigo: #1f2380;
    --indigo-light: #2e34a6;
    --button: #0c2a5e;
    --logo-blue: #173f7c;
    --light-band: #c9d3de;
    --photo-light: #dfe4ea;
    --photo-mid: #b9c2cc;
    --white: #ffffff;
    --body-ink: #1c1c24;
  }
  * { box-sizing: border-box; margin: 0; padding: 0; }
  html, body { width: 1200px; height: 1200px; overflow: hidden; }
  body {
    background: var(--board);
    font-family: "Source Sans 3", "Helvetica Neue", Arial, sans-serif;
    position: relative;
  }
  .board-logo {
    position: absolute; left: 968px; top: 28px;
    font-size: 50px; font-weight: 400; color: var(--logo-blue);
    letter-spacing: 1px; line-height: 1;
  }
  .ad {
    position: absolute; width: 536px; height: 280px; overflow: hidden;
    box-shadow: 4px 8px 10px rgba(0,0,0,0.35);
    color: var(--white);
  }
  .col-left { left: 49px; }
  .col-right { left: 615px; }
  .row-1 { top: 116px; }
  .row-2 { top: 442px; }
  .row-3 { top: 767px; }

  .ad-bg { position: absolute; inset: 0; }
  .ad > .t { position: absolute; white-space: nowrap; line-height: 1; }
  .kicker { font-size: 17px; font-style: italic; font-weight: 300; }
  .title { font-size: 23px; font-weight: 700; }
  .subtitle { font-size: 20px; font-style: italic; font-weight: 300; }
  .date { font-size: 23px; font-weight: 700; }

  .headshot {
    position: absolute; border-radius: 50%;
    background: radial-gradient(circle at 50% 40%, #9a9a9a 0%, #5f5f5f 55%, #d8d8d8 100%);
    box-shadow: 2px 3px 6px rgba(0,0,0,0.45);
  }
  .logo-mark {
    position: absolute; color: var(--logo-blue);
    font-size: 27px; font-weight: 400; line-height: 1; letter-spacing: 0.5px;
  }
  .cta {
    position: absolute; height: 30px; width: 161px; border-radius: 15px;
    background: var(--button); color: var(--white);
    font-size: 18px; font-weight: 400; line-height: 30px; text-align: center;
    box-shadow: 2px 3px 4px rgba(0,0,0,0.4);
  }
  .host-bar {
    position: absolute; left: 0; right: 0; top: 221px; height: 59px;
    background: linear-gradient(90deg, #c6d0da, #dfe5eb 60%, #c7d1dc);
  }
  .host-strip {
    position: absolute; left: 0; right: 0; top: 205px; height: 16px;
  }
  .hosts {
    position: absolute; left: 119px; top: 231px;
    font-size: 10.5px; font-style: italic; line-height: 13.5px; color: #1a1a22;
  }
  .caption {
    position: absolute; left: 60px; right: 60px; top: 1097px;
    font-size: 21px; font-style: italic; font-weight: 300; line-height: 26px;
    text-align: center; color: var(--body-ink);
  }
</style>
</head>
<body>

<div class="board-logo">ZEMBO</div>

<!-- Row 1 left: navy split -->
<section class="ad col-left row-1">
  <svg class="ad-bg" width="536" height="280" viewBox="0 0 536 280">
    <defs>
      <linearGradient id="photoCool" x1="0" y1="0" x2="1" y2="1">
        <stop offset="0" stop-color="#e8ecf1"/><stop offset="1" stop-color="#aeb9c6"/>
      </linearGradient>
    </defs>
    <rect width="536" height="280" fill="url(#photoCool)" role="img" aria-label="Abstract architectural photo background"/>
    <polygon points="0,0 266,0 330,280 0,280" fill="var(--navy-mid)"/>
    <polygon points="0,0 250,0 314,280 0,280" fill="var(--navy)"/>
  </svg>
  <div class="t kicker" style="left:8px;top:13px">Free Live Webinar:</div>
  <div class="t title" style="left:8px;top:36px">"Cybersecurity Starts</div>
  <div class="t title" style="left:114px;top:65px">at the Top"</div>
  <div class="t subtitle" style="left:12px;top:126px">How to 'sell' a cybersecurity</div>
  <div class="t subtitle" style="left:12px;top:152px">strategy internally</div>
  <div class="t date" style="left:12px;top:205px">Wednesday,</div>
  <div class="t date" style="left:12px;top:233px">June 12th at 1pm EST</div>
  <div class="headshot" role="img" aria-label="Headshot of host Tom Harlow" style="left:285px;top:7px;width:126px;height:126px"></div>
  <div class="headshot" role="img" aria-label="Headshot of host Ivan Petrakov" style="left:408px;top:102px;width:116px;height:116px"></div>
  <div class="logo-mark" style="left:436px;top:34px">ZEMBO</div>
  <div class="cta" style="left:354px;top:240px">Book Your Place</div>
</section>

<!-- Row 1 right: navy with host bar -->
<section class="ad col-right row-1">
  <div class="ad-bg" style="background:var(--navy)"></div>
  <div class="host-strip" style="background:#1a3f80"></div>
  <div class="host-bar"></div>
  <div class="t kicker" style="left:13px;top:27px">Munch &amp; Learn Webinar:</div>
  <div class="t title" style="left:13px;top:50px">"Cybersecurity Starts</div>
  <div class="t title" style="left:119px;top:79px">at the Top"</div>
  <div class="headshot" role="img" aria-label="Headshot of host Tom Harlow" style="left:267px;top:12px;width:116px;height:116px"></div>
  <div class="headshot" role="img" aria-label="Headshot of host Ivan Petrakov" style="left:402px;top:12px;width:116px;height:116px"></div>
  <div class="t subtitle" style="left:18px;top:133px">Learn about the latest cybersecurity trends from industry experts</div>
  <div class="t date" style="right:17px;top:166px">Wednesday, June 12th at 1pm EST</div>
  <div class="logo-mark" style="left:16px;top:240px">ZEMBO</div>
  <div class="hosts">Your hosts: Tom Harlow, Cybersecurity Practice Lead<br>and Ivan Petrakov, Information, Security and<br>Compliance Director</div>
  <div class="cta" style="left:358px;top:238px">Reserve Your Place</div>
</section>

<!-- Row 2 left: black split -->
<section class="ad col-left row-2">
  <svg class="ad-bg" width="536" height="280" viewBox="0 0 536 280">
    <defs>
      <linearGradient id="photoGrey" x1="0" y1="0" x2="1" y2="1">
        <stop offset="0" stop-color="#f0f0f0"/><stop offset="1" stop-color="#9a9a9a"/>
      </linearGradient>
    </defs>
    <rect width="536" height="280" fill="url(#photoGrey)" role="img" aria-label="Monochrome skyscraper photo background"/>
    <polygon points="0,0 260,0 328,280 0,280" fill="var(--ink-black)"/>
  </svg>
  <div class="t kicker" style="left:12px;top:12px">Munch &amp; Learn Webinar:</div>
  <div class="t title" style="left:12px;top:36px">"Cybersecurity Starts</div>
  <div class="t title" style="left:119px;top:65px">at the Top"</div>
  <div class="t subtitle" style="left:17px;top:112px">Your step-by step guide to</div>
  <div class="t subtitle" style="left:17px;top:138px">implementing a cybersecurity</div>
  <div class="t subtitle" style="left:17px;top:163px">strategy</div>
  <div class="t date" style="left:17px;top:204px">Wednesday,</div>
  <div class="t date" style="left:17px;top:233px">June 12th at 1pm EST</div>
  <div class="headshot" role="img" aria-label="Headshot of host Tom Harlow" style="left:290px;top:7px;width:126px;height:126px"></div>
  <div class="headshot" role="img" aria-label="Headshot of host Ivan Petrakov" style="left:413px;top:102px;width:116px;height:116px"></div>
  <div class="logo-mark" style="left:440px;top:23px">ZEMBO</div>
  <div class="cta" style="left:359px;top:239px">Reserve Your Place</div>
</section>

<!-- Row 2 right: black with host bar -->
<section class="ad col-right row-2">
  <div class="ad-bg" style="background:var(--ink-black)"></div>
  <div class="host-strip" style="background:#2a2a2e"></div>
  <div class="host-bar"></div>
  <div class="t title" style="left:13px;top:21px">"Cybersecurity Starts</div>
  <div class="t title" style="left:119px;top:50px">at the Top"</div>
  <div class="headshot" role="img" aria-label="Headshot of host Tom Harlow" style="left:267px;top:12px;width:116px;height:116px"></div>
  <div class="headshot" role="img" aria-label="Headshot of host Ivan Petrakov" style="left:402px;top:12px;width:116px;height:116px"></div>
  <div class="t subtitle" style="left:13px;top:105px">Learn how to build an effective</div>
  <div class="t subtitle" style="left:13px;top:129px">cybersecruity strategy from the top down</div>
  <div class="t date" style="right:17px;top:164px">Wednesday, June 12th at 1pm EST</div>
  <div class="logo-mark" style="left:16px;top:240px">ZEMBO</div>
  <div class="hosts">Your hosts: Tom Harlow, Cybersecurity Practice Lead<br>and Ivan Petrakov, Information, Security and<br>Compliance Director</div>
  <div class="cta" style="left:358px;top:238px">Reserve Your Place</div>
</section>

<!-- Row 3 left: indigo split -->
<section class="ad col-left row-3">
  <svg class="ad-bg" width="536" height="280" viewBox="0 0 536 280">
    <defs>
      <linearGradient id="photoSteel" x1="0" y1="0" x2="1" y2="1">
        <stop offset="0" stop-color="#9a9a9a"/><stop offset="0.5" stop-color="#e6e6e6"/><stop offset="1" stop-color="#8c8c8c"/>
      </linearGradient>
      <linearGradient id="indigoFade" x1="0" y1="0" x2="1" y2="0">
        <stop offset="0" stop-color="#15185e"/><stop offset="1" stop-color="var(--indigo)"/>
      </linearGradient>
    </defs>
    <rect width="536" height="280" fill="url(#photoSteel)" role="img" aria-label="Monochrome modern building facade photo background"/>
    <polygon points="0,0 276,0 330,280 0,280" fill="var(--indigo-light)"/>
    <polygon points="0,0 260,0 300,280 0,280" fill="url(#indigoFade)"/>
  </svg>
  <div class="t kicker" style="left:13px;top:12px">Munch &amp; Learn Webinar:</div>
  <div class="t title" style="left:13px;top:36px">"Cybersecurity Starts</div>
  <div class="t title" style="left:120px;top:65px">at the Top"</div>
  <div class="t subtitle" style="left:17px;top:113px">Learn how to defend your</div>
  <div class="t subtitle" style="left:17px;top:137px">organization from cyber</div>
  <div class="t subtitle" style="left:17px;top:161px">threats with top industry experts</div>
  <div class="t date" style="left:17px;top:203px">Wednesday,</div>
  <div class="t date" style="left:17px;top:232px">June 12th at 1pm EST</div>
  <div class="headshot" role="img" aria-label="Headshot of host Tom Harlow" style="left:290px;top:7px;width:126px;height:126px"></div>
  <div class="headshot" role="img" aria-label="Headshot of host Ivan Petrakov" style="left:413px;top:102px;width:116px;height:116px"></div>
  <div class="logo-mark" style="left:440px;top:23px">ZEMBO</div>
  <div class="cta" style="left:359px;top:239px">Book Your Place</div>
</section>

<!-- Row 3 right: indigo with host bar -->
<section class="ad col-right row-3">
  <div class="ad-bg" style="background:var(--indigo)"></div>
  <div class="host-strip" style="background:#3038a8"></div>
  <div class="host-bar"></div>
  <div class="t title" style="left:13px;top:21px">"Cybersecurity Starts</div>
  <div class="t title" style="left:119px;top:50px">at the Top"</div>
  <div class="headshot" role="img" aria-label="Headshot of host Tom Harlow" style="left:267px;top:12px;width:116px;height:116px"></div>
  <div class="headshot" role="img" aria-label="Headshot of host Ivan Petrakov" style="left:402px;top:12px;width:116px;height:116px"></div>
  <div class="t subtitle" style="left:18px;top:105px">How do you get started with</div>
  <div class="t subtitle" style="left:18px;top:129px">cybersecurity?</div>
  <div class="t date" style="right:17px;top:164px">Wednesday, June 12th at 1pm EST</div>
  <div class="logo-mark" style="left:16px;top:240px">ZEMBO</div>
  <div class="hosts">Your hosts: Tom Harlow, Cybersecurity Practice Lead<br>and Ivan Petrakov, Information, Security and<br>Compliance Director</div>
  <div class="cta" style="left:358px;top:238px">Reserve Your Place</div>
</section>

<p class="caption">Lorem ipsum dolor sit amet, consectetuer adipiscing elit, sed diam nonummy nibh euismod tincidunt ut laoreet dolore magna aliquam erat volutpat. Ut wisi enim ad minim veniam, quis nostrud exerci tation ullamcorper suscipit lobortis nisl ut aliquip ex ea commodo consequat.</p>

</body>
</html>
```